Professional DJ Business Card

Business card for giving out to clubs and venues or interested groups that are in need of a professional DJ. I want something artistic and catchy/alluring, with a minimalist approach that gets just the vital amount of info and leaves the rest for inquiry via contacting me. Ideally I would like one side to have an image of something cool like an eye and my name, then the other side be the contact info, I am definitely feeling a black or dark colored card, but I am open to other designs. I am uploading a picture that I made that reflects a little of what I am *kind of* looking for.

Industry/Entity Type

Business

Contact Information for Business Card

Tomas Halvik (Voxtel)
Professional DJ (West Coast)
EDM (Deep/House/Techno), Hip Hop, Latin, Trap.
Cell: 555-274-9163
Email: Voxtelofficial@mailnest.net
www.beatcloudia.net/yourtuneisfading

```html
<!DOCTYPE html>
<html lang="en">
<head>
<meta charset="utf-8">
<title>Voxtel – DJ Business Card</title>
<link href="https://fonts.googleapis.com/css2?family=Open+Sans:wght@400;600;700&display=swap" rel="stylesheet">
<style>
  :root {
    --ink-black: #0d0d0d;
    --card-white: #f4f4f4;
    --accent-red: #d23a52;
    --text-dark: #1f1f1f;
    --text-grey: #4a4a4a;
    --stage: #d9d6d1;
  }
  html, body {
    margin: 0;
    padding: 0;
    width: 1200px;
    height: 1062px;
    overflow: hidden;
    background: var(--stage);
    font-family: "Open Sans", Arial, sans-serif;
  }
  .sheet {
    position: relative;
    width: 1200px;
    height: 1062px;
  }
  .card {
    position: absolute;
    left: 320px;
    width: 560px;
    height: 320px;
    border-radius: 4px;
    overflow: hidden;
    box-shadow: 0 10px 30px rgba(0,0,0,0.25);
  }
  .card--front { top: 150px; background: var(--ink-black); }
  .card--back {
    top: 590px;
    background: linear-gradient(160deg, #2c2c2c 0%, #141414 45%, #050505 100%);
  }
  .card-frame { position: absolute; inset: 0; }
  .front-content {
    position: absolute;
    left: 118px;
    top: 38px;
    width: 340px;
  }
  .wordmark {
    display: flex;
    align-items: center;
    gap: 12px;
    font-weight: 700;
    letter-spacing: 4px;
    text-transform: uppercase;
  }
  .wordmark--front {
    color: var(--text-dark);
    font-size: 46px;
    margin-bottom: 18px;
  }
  .wordmark-dot {
    width: 16px;
    height: 16px;
    border-radius: 50%;
    background: var(--accent-red);
    flex: none;
  }
  .holder-name {
    color: var(--accent-red);
    font-weight: 600;
    font-size: 20px;
    margin: 0 0 4px;
  }
  .holder-line {
    color: var(--text-grey);
    font-size: 12.5px;
    margin: 0 0 3px;
  }
  .contact-list {
    list-style: none;
    margin: 8px 0 0;
    padding: 0;
  }
  .contact-item {
    display: flex;
    align-items: center;
    gap: 8px;
    color: var(--text-grey);
    font-size: 12.5px;
    margin-bottom: 4px;
  }
  .contact-icon { width: 12px; height: 12px; flex: none; }
  .back-content {
    position: absolute;
    inset: 0;
    display: flex;
    align-items: center;
    justify-content: center;
  }
  .wordmark--back {
    color: #ffffff;
    font-size: 72px;
  }
</style>
</head>
<body>
<main class="sheet">

  <section class="card card--front" aria-label="Business card front with contact details">
    <svg class="card-frame" viewBox="0 0 560 320" width="560" height="320" aria-hidden="true">
      <defs>
        <clipPath id="frontClip"><rect width="560" height="320"/></clipPath>
      </defs>
      <g clip-path="url(#frontClip)">
        <rect width="560" height="320" fill="var(--ink-black)"/>
        <ellipse cx="280" cy="160" rx="262" ry="300" fill="var(--card-white)"/>
        <ellipse cx="280" cy="160" rx="250" ry="292" fill="none" stroke="var(--accent-red)" stroke-width="4"/>
      </g>
    </svg>

    <div class="front-content">
      <div class="wordmark wordmark--front">
        <span class="wordmark-dot"></span>Voxtel
      </div>
      <p class="holder-name">Tomas Halvik (Voxtel)</p>
      <p class="holder-line">Professional DJ (West Coast)</p>
      <p class="holder-line">EDM (Deep/House/Techno), Hip Hop, Latin, Trap.</p>
      <ul class="contact-list">
        <li class="contact-item">
          <svg class="contact-icon" viewBox="0 0 12 12" aria-hidden="true"><path d="M2.5 1 L4.5 1 L5 3.5 L3.8 4.5 Q4.8 6.8 7.3 8 L8.3 6.9 L11 7.5 L11 9.5 Q11 11 9.5 11 Q1 10 1 2.5 Q1 1 2.5 1Z" fill="var(--accent-red)"/></svg>
          555-274-9163
        </li>
        <li class="contact-item">
          <svg class="contact-icon" viewBox="0 0 12 12" aria-hidden="true"><g fill="none" stroke="var(--accent-red)" stroke-width="1"><circle cx="6" cy="6" r="5"/><ellipse cx="6" cy="6" rx="2.2" ry="5"/><line x1="1" y1="6" x2="11" y2="6"/></g></svg>
          www.beatcloudia.net/yourtuneisfading
        </li>
        <li class="contact-item">
          <svg class="contact-icon" viewBox="0 0 12 12" aria-hidden="true"><circle cx="6" cy="6" r="6" fill="var(--accent-red)"/><text x="6" y="9" text-anchor="middle" font-size="8.5" font-weight="700" fill="#fff" font-family="Open Sans, Arial, sans-serif">@</text></svg>
          Voxtelofficial@mailnest.net
        </li>
      </ul>
    </div>
  </section>

  <section class="card card--back" aria-label="Business card back with name">
    <div class="back-content">
      <div class="wordmark wordmark--back">
        <span class="wordmark-dot"></span>Voxtel
      </div>
    </div>
  </section>

</main>
</body>
</html>
```